Unique Business Card Design

Unique Business Card design for our orthotic and prosthetic company. Our logo is on our website, color is light blue. Unique shape (artificial leg shaped, vertical, etc..) preferred. Logo, business name, individual name and basic demographics needed.

Industry/Entity Type

Business

Contact Information for Business Card

Logo, Industry, Phone # Logo, "Prosthetic & Orthotic Services" Place to add individual name and contact info

Colors
cee9f5

Requirements
Must have
• The icon must be there, placement of "Prosthetic & Orthotic Services" can be moved
Nice to have
• Like the mix of light blue, and a little darker blue. One design included the icons from my website which was a nice touch

```html
<!DOCTYPE html>
<html lang="en">
<head>
<meta charset="utf-8">
<title>Stridewell Inc. Business Card</title>
<link href="https://fonts.googleapis.com/css2?family=Libre+Franklin:wght@400;500;700&family=Crimson+Text:ital,wght@1,600&display=swap" rel="stylesheet">
<style>
  :root {
    --page-bg: #e6e6e8;
    --card-white: #f7f7f8;
    --navy: #23398c;
    --band-dark: #1d327f;
    --band-mid: #2a45a0;
    --text-light: #f2f4fa;
    --text-muted: #b7bfd8;
    --text-fax: #c9b39a;
    --divider: #8e9ac4;
    --silhouette: #e4e6ee;
  }
  * { margin: 0; padding: 0; box-sizing: border-box; }
  html, body {
    width: 1200px; height: 834px; overflow: hidden;
    background: var(--page-bg);
  }
  .card {
    position: absolute; left: 200px; top: 189px;
    width: 800px; height: 456px;
    background: var(--card-white);
    border-radius: 14px; overflow: hidden;
    box-shadow: 0 6px 18px rgba(0,0,0,0.18);
    font-family: "Libre Franklin", Arial, sans-serif;
  }
  .brand-mark {
    position: absolute; left: 36px; top: 36px;
    width: 114px; height: 114px; border-radius: 50%;
    background: var(--navy);
  }
  .brand-name {
    position: absolute; left: 178px; top: 58px;
    font-size: 33px; font-weight: 700; color: var(--navy);
    letter-spacing: -0.5px; white-space: nowrap;
  }
  .brand-rule {
    position: absolute; left: 183px; top: 99px;
    width: 276px; height: 2px; background: var(--navy);
  }
  .tagline {
    position: absolute; left: 183px; top: 106px; width: 276px;
    text-align: center;
    font-family: "Crimson Text", Georgia, serif;
    font-style: italic; font-weight: 600; font-size: 19px;
    color: var(--navy);
  }
  .info-band {
    position: absolute; left: 0; top: 189px;
    width: 800px; height: 245px;
    background: linear-gradient(100deg, var(--band-dark) 0%, var(--band-mid) 55%, var(--band-dark) 100%);
  }
  .person-name {
    position: absolute; left: 44px; top: 30px;
    font-size: 24px; font-weight: 500; color: var(--text-light);
  }
  .person-name .credentials { font-size: 19px; }
  .person-email {
    position: absolute; left: 44px; top: 70px;
    font-size: 19px; color: var(--text-light);
  }
  .phone-list {
    position: absolute; left: 44px; top: 124px; list-style: none;
  }
  .phone-list li {
    display: flex; align-items: center; height: 31px;
    font-size: 18px; color: var(--text-muted);
  }
  .phone-list li.fax { color: var(--text-fax); }
  .phone-list svg { width: 18px; height: 20px; margin-right: 21px; fill: currentColor; }
  .divider {
    position: absolute; left: 243px; top: 127px;
    width: 1px; height: 83px; background: var(--divider);
  }
  .address {
    position: absolute; left: 265px; top: 124px;
    font-size: 18px; line-height: 31px; color: var(--text-muted);
  }
  .figure-art {
    position: absolute; left: 662px; top: 0;
    width: 118px; height: 245px; border-radius: 50px 50px 10px 10px;
    background: linear-gradient(180deg, var(--silhouette), #cdd2e2);
  }
</style>
</head>
<body>
  <div class="card">
    <div class="brand-mark"></div>
    <div class="brand-name">STRIDEWELL INC.</div>
    <div class="brand-rule"></div>
    <div class="tagline">Prosthetic &amp; Orthotic Services</div>

    <div class="info-band">
      <div class="person-name">Mara Kessler<span class="credentials">, CO LPO</span></div>
      <div class="person-email">Mkessler@stridewellinc.com</div>

      <ul class="phone-list">
        <li>
          <svg viewBox="0 0 18 20" aria-hidden="true"><path d="M1 6c0-3 4-4 8-4s8 1 8 4v2h-4V6H5v2H1z"/><rect x="3" y="9" width="12" height="9" rx="2"/></svg>
          555.201.4800
        </li>
        <li>
          <svg viewBox="0 0 18 20" aria-hidden="true"><path d="M5 1h8a1 1 0 0 1 1 1v16a1 1 0 0 1-1 1H5a1 1 0 0 1-1-1V2a1 1 0 0 1 1-1zm1 2v12h6V3z"/></svg>
          555.201.4932
        </li>
        <li class="fax">
          <svg viewBox="0 0 18 20" aria-hidden="true"><rect x="4" y="3" width="10" height="6"/><rect x="1" y="9" width="16" height="8" rx="1"/></svg>
          555-318.6027
        </li>
      </ul>

      <div class="divider"></div>

      <div class="address">
        2290 W. 14th St.,<br>
        Lakeview, NY 10450<br>
        www.stridewellinc.com
      </div>

      <div class="figure-art" role="img" aria-label="Light silhouette of a standing human figure"></div>
    </div>
  </div>
</body>
</html>
```